Healer at the Hearth needs business card

We need a business card that reflects the look and feel of the new website at www.healerathearth.ca

Target Market(s)

Our patient navigation and advocacy services are most commonly used by seniors who feel overwhelmed by the health care system and want someone on their side to advocate for their care. Individuals with ill parents or other family members may also come to rely on Healer at the Hearth to help them support their loved one through their health care journey. Ultimately, anyone who finds their health care experience challenging and wants someone completely focused on their needs can benefit from the services of our doctor / nurse team.

Industry/Entity Type

Business

Requirements
Must have
• One design tailored for two clinician which should include: logo, name, title, tel, email, web address and tagline
Nice to have
• A banner image to create a similar look to the website at www.healerathearth.ca
Should not have
• Too cluttered or busy - must be clean and professional

```html
<!DOCTYPE html>
<html lang="en">
<head>
<meta charset="utf-8">
<title>Healer at the Hearth – Business Card</title>
<link href="https://fonts.googleapis.com/css2?family=Ubuntu:wght@400;500&display=swap" rel="stylesheet">
<style>
  :root {
    --backdrop: #e9e7e4;
    --card: #ffffff;
    --ink-blue: #3f6d9c;
    --accent-red: #c3262d;
    --soft-salmon: #e39a86;
    --card-shadow: rgba(40, 30, 20, 0.18);
  }
  html, body {
    margin: 0;
    padding: 0;
    overflow: hidden;
  }
  body {
    width: 1200px;
    height: 873px;
    background: var(--backdrop);
    display: flex;
    align-items: center;
    justify-content: center;
    gap: 60px;
    font-family: "Ubuntu", sans-serif;
  }
  .card {
    position: relative;
    width: 490px;
    height: 280px;
    background: var(--card);
    box-shadow: 0 10px 28px var(--card-shadow);
    overflow: hidden;
  }
  /* Contact side */
  .card-contact .corner-shape {
    position: absolute;
    border-radius: 50%;
    background: var(--soft-salmon);
  }
  .card-contact .corner-shape.top-left {
    width: 130px;
    height: 130px;
    left: -60px;
    top: -60px;
  }
  .card-contact .corner-shape.bottom-right {
    width: 150px;
    height: 150px;
    right: -55px;
    bottom: -60px;
  }
  .contact-block {
    position: absolute;
    left: 110px;
    top: 58px;
    color: var(--ink-blue);
  }
  .person-name {
    margin: 0;
    font-size: 25px;
    font-weight: 400;
    letter-spacing: 0.2px;
  }
  .person-title {
    margin: 6px 0 24px;
    font-size: 15px;
    color: var(--soft-salmon);
    letter-spacing: 0.5px;
  }
  .contact-list {
    list-style: none;
    margin: 0;
    padding: 0;
  }
  .contact-item {
    display: flex;
    align-items: center;
    gap: 10px;
    font-size: 18px;
    line-height: 30px;
  }
  .contact-icon {
    width: 16px;
    height: 16px;
    flex: none;
  }
  /* Brand side */
  .card-brand {
    display: flex;
    align-items: center;
    justify-content: center;
  }
  .brand-lockup {
    display: flex;
    align-items: center;
    gap: 16px;
  }
  .brand-dot {
    width: 52px;
    height: 52px;
    border-radius: 50%;
    background: var(--accent-red);
  }
  .brand-name {
    margin: 0;
    font-size: 30px;
    font-weight: 400;
    line-height: 1.05;
    color: var(--ink-blue);
  }
</style>
</head>
<body>

  <section class="card card-contact" aria-label="Business card, contact side">
    <div class="corner-shape top-left"></div>
    <div class="corner-shape bottom-right"></div>
    <div class="contact-block">
      <h1 class="person-name">Martin Keloway, MD</h1>
      <p class="person-title">Co-Founder</p>
      <ul class="contact-list">
        <li class="contact-item">
          <svg class="contact-icon" viewBox="0 0 16 16" aria-hidden="true">
            <path d="M4 1.5 L6.5 4.5 L5 6.2 C5.8 8 7.8 10 9.8 11 L11.5 9.5 L14.5 12 L12.6 14.3 C7 13.5 2.5 9 1.7 3.4 Z" fill="var(--accent-red)"/>
          </svg>
          <span>555-014-2298</span>
        </li>
        <li class="contact-item">
          <svg class="contact-icon" viewBox="0 0 16 16" aria-hidden="true">
            <circle cx="8" cy="8" r="3" fill="none" stroke="var(--accent-red)" stroke-width="2"/>
            <path d="M11 5 V9.5 C11 11.5 14.5 11.5 14.5 8 A6.5 6.5 0 1 0 11 13.8" fill="none" stroke="var(--accent-red)" stroke-width="2"/>
          </svg>
          <span>info@healerathearth.ca</span>
        </li>
        <li class="contact-item">
          <svg class="contact-icon" viewBox="0 0 16 16" aria-hidden="true">
            <circle cx="8" cy="8" r="7.5" fill="var(--accent-red)"/>
            <g fill="none" stroke="#fff" stroke-width="1">
              <ellipse cx="8" cy="8" rx="3" ry="7"/>
              <line x1="1" y1="8" x2="15" y2="8"/>
              <line x1="2" y1="4.5" x2="14" y2="4.5"/>
              <line x1="2" y1="11.5" x2="14" y2="11.5"/>
            </g>
          </svg>
          <span>www.healerathearth.ca</span>
        </li>
      </ul>
    </div>
  </section>

  <section class="card card-brand" aria-label="Business card, brand side">
    <div class="brand-lockup">
      <div class="brand-dot"></div>
      <h2 class="brand-name">Healer at<br>the Hearth</h2>
    </div>
  </section>

</body>
</html>
```